Design some Business Cards for Meadow 4

Hello I need a fresh looking biz card design. I attached the logo. I need the top swirl in the tornado to be a bright color, not sure what would look best. The information needed is:
Felix Randerhill
508-761-2094
felix@pelnorta.com

I will give 5 star rating. Thank you

```html
<!DOCTYPE html>
<html lang="en">
<head>
<meta charset="utf-8">
<title>Meadow 4 Business Card</title>
<link href="https://fonts.googleapis.com/css2?family=Source+Sans+3:wght@400;600&display=swap" rel="stylesheet">
<style>
  :root {
    --backdrop: #555555;
    --card-front: #ffffff;
    --card-back: #dcdcdc;
    --ink: #1a1a1a;
    --muted: #333333;
    --accent-red: #e31b23;
    --accent-blue: #2f7fd6;
  }
  * { margin: 0; padding: 0; box-sizing: border-box; }
  html, body {
    width: 1200px; height: 393px; overflow: hidden;
    background: var(--backdrop);
    font-family: "Source Sans 3", "Myriad Pro", sans-serif;
  }
  .sheet { position: relative; width: 1200px; height: 393px; }
  .card {
    position: absolute; top: 27px; height: 327px;
  }
  .card--front { left: 42px; width: 533px; background: var(--card-front); }
  .card--back { left: 623px; width: 540px; background: var(--card-back); }

  .holder-name {
    position: absolute; left: 44px; top: 94px;
    font-size: 22px; color: var(--ink); font-weight: 400;
  }
  .brand {
    position: absolute; display: flex; align-items: center; gap: 12px;
  }
  .brand__dot {
    width: 30px; height: 30px; border-radius: 50%;
    background: var(--accent-red);
  }
  .brand__name {
    font-size: 46px; font-weight: 600; color: var(--ink); line-height: 1;
  }
  .card--front .brand { left: 228px; top: 168px; }
  .card--back .brand { left: 0; right: 0; top: 138px; justify-content: center; }

  .stripes { position: absolute; left: 0; top: 248px; width: 533px; height: 18px; }

  .contact {
    position: absolute; top: 293px; display: flex; align-items: center; gap: 8px;
    font-size: 16px; color: var(--muted);
  }
  .contact--phone { left: 62px; }
  .contact--email { left: 298px; }
  .contact svg { display: block; }
</style>
</head>
<body>
<div class="sheet">
  <section class="card card--front">
    <p class="holder-name">Felix Randerhill</p>

    <div class="brand">
      <span class="brand__dot"></span>
      <span class="brand__name">Meadow 4</span>
    </div>

    <svg class="stripes" viewBox="0 0 533 18" aria-hidden="true">
      <polygon points="0,0 270,0 262,7 0,7" fill="var(--accent-red)"/>
      <polygon points="276,0 533,0 533,7 268,7" fill="var(--accent-blue)"/>
      <polygon points="0,10 259,10 257,12 0,12" fill="var(--accent-red)"/>
      <polygon points="265,10 533,10 533,12 263,12" fill="var(--accent-blue)"/>
    </svg>

    <div class="contact contact--phone">
      <svg width="16" height="12" viewBox="0 0 16 12" aria-hidden="true">
        <path d="M1 4 Q8 -1 15 4 L13 6 L11 4.5 L5 4.5 L3 6 Z" fill="#777"/>
        <rect x="3" y="6" width="10" height="6" rx="1" fill="#777"/>
      </svg>
      <span>508-761-2094</span>
    </div>
    <div class="contact contact--email">
      <svg width="16" height="11" viewBox="0 0 16 11" aria-hidden="true">
        <rect x="0.5" y="0.5" width="15" height="10" fill="#888"/>
        <path d="M0.5 0.5 L8 6 L15.5 0.5" fill="none" stroke="#fff" stroke-width="1"/>
      </svg>
      <span>felix@pelnorta.com</span>
    </div>
  </section>

  <section class="card card--back">
    <div class="brand">
      <span class="brand__dot"></span>
      <span class="brand__name">Meadow 4</span>
    </div>
  </section>
</div>
</body>
</html>
```